KerrLow Farm

Need a nice simple clean double sided business card that has our logo and info on:
Kerr Low Farm
Martin & Felicity Kerr Low
kerrlowfarm@mailbarn.example
Martin: 1-780-555-0148
Felicity: 1-780-555-0193
Instagram @ kerrlow_farm

Contact Information for Business Card

Martin & Felicity Kerr Low kerrlowfarm@mailbarn.example Martin: 1-780-555-0148 Felicity: 1-780-555-0193

```html
<!DOCTYPE html>
<html lang="en">
<head>
<meta charset="utf-8">
<title>Kerr Low Farm – Business Card</title>
<link href="https://fonts.googleapis.com/css2?family=Alegreya+SC&family=Cormorant+Garamond:wght@500&display=swap" rel="stylesheet">
<style>
  :root {
    --page: #ffffff;
    --frame: #b9b9b9;
    --leaf: #a4e022;
    --leaf-deep: #6a9e1a;
    --name-green: #8cc63f;
    --harvest: #e8892a;
    --ink: #2b2b2b;
    --paper: #ffffff;
    --shadow: rgba(0, 0, 0, 0.28);
  }
  * { box-sizing: border-box; margin: 0; padding: 0; }
  html, body { width: 1200px; height: 636px; overflow: hidden; background: var(--page); }
  .sheet {
    position: relative;
    width: 1200px; height: 636px;
    border: 1px solid var(--frame);
  }
  .card {
    position: absolute;
    top: 151px;
    width: 540px; height: 315px;
    box-shadow: 6px 8px 8px var(--shadow);
    overflow: hidden;
  }
  .card-front { left: 45px; background: var(--paper); border: 1px solid #9a9a9a; }
  .card-back { left: 630px; background: var(--leaf); }

  .brand { position: absolute; text-align: center; }
  .brand-ring {
    display: block; margin: 0 auto;
    border-radius: 50%;
  }
  .brand-name {
    font-family: "Cormorant Garamond", serif;
    font-weight: 500;
    text-transform: uppercase;
    white-space: nowrap;
    line-height: 1;
  }
  .card-front .brand { left: 38px; top: 72px; width: 218px; }
  .card-front .brand-ring { width: 86px; height: 86px; border: 3px solid var(--leaf-deep); }
  .card-front .brand-name { color: var(--leaf-deep); font-size: 29px; margin-top: 8px; }

  .card-back .brand { left: 120px; top: 74px; width: 300px; }
  .card-back .brand-ring { width: 102px; height: 102px; border: 3px solid var(--paper); }
  .card-back .brand-name { color: var(--paper); font-size: 37px; margin-top: 14px; }

  .contact {
    position: absolute; left: 333px; top: 98px;
    font-family: "Alegreya SC", serif;
    color: var(--ink);
  }
  .contact-owners { color: var(--name-green); font-size: 14px; letter-spacing: 0.2px; white-space: nowrap; }
  .contact-list {
    list-style: none;
    margin-top: 13px;
    font-size: 12.5px;
    line-height: 18.6px;
    white-space: nowrap;
  }
  .contact-rule {
    position: absolute; left: 317px; top: 136px;
    width: 1px; height: 63px; background: var(--name-green);
  }
  .stripe-harvest { position: absolute; left: 0; right: 0; top: 292px; height: 3px; background: var(--harvest); }
  .stripe-leaf { position: absolute; left: 0; right: 0; top: 295px; bottom: 0; background: var(--leaf); }
</style>
</head>
<body>
<main class="sheet">
  <section class="card card-front" aria-label="Card front">
    <div class="brand">
      <span class="brand-ring"></span>
      <p class="brand-name">Kerr Low Farm</p>
    </div>
    <span class="contact-rule"></span>
    <div class="contact">
      <p class="contact-owners">Martin &amp; Felicity Kerr Low</p>
      <ul class="contact-list">
        <li>kerrlowfarm@mailbarn.example</li>
        <li>Martin:&nbsp; 1-780-555-0148</li>
        <li>Felicity:&nbsp; 1-780-555-0193</li>
        <li>Instagram @kerrlow_farm</li>
      </ul>
    </div>
    <span class="stripe-harvest"></span>
    <span class="stripe-leaf"></span>
  </section>

  <section class="card card-back" aria-label="Card back">
    <div class="brand">
      <span class="brand-ring"></span>
      <p class="brand-name">Kerr Low Farm</p>
    </div>
  </section>
</main>
</body>
</html>
```